Re-design of a website for Jewellery Store

We need a design for a jewellery store that will be on Shopify.

The website is going to be on Shopify and we will install a new theme and we need to create new designs, based on a similar layout to the theme so we can simply customise the theme colours and banners etc to fit the layout of the theme.

We have a link of the old website that we need to improve and make better.

We need a slick modern design and can use photos of his jewellery etc.

Here are three themes we think are good for us

https://morvanti-gems.example-shop.com/collections/featured
https://pellwick-01.example-shop.com/
https://vistune-demo.example-shop.com/

Here's a few websites I like the look and function of below with notes. But
open to hearing your opinions and ideas.

https://www.fernandquill.example/ - I like the main page as there is a little
more going on. I also like the layout of the stock pages and how simple this
is to view the jewellery.

https://www.miriamholte.example/nz/jewellery/all-jewellery/harbour-crest-ring-g
old-mh582t4p/gold - I like this website layout the best for stock. I think
it is really simple to view all items. I like best once you click into a
stock piece the layout on the attached link of the individual options and
price options for each piece.

https://tollandpine.example.au/pages/contact-us - I like the contact us page with
more detail the customer has to fill in about what the are enquiring about.

https://www.oritaandbrisk.example.nz/bespoke-designs/ - I like the page
dedicated to "one off" custom designs that we can showcase more like a
gallery separate to our stock in store to give customers ideas if they
wanted to book an appointment to design their own ring.
Updates

Once somebody shows interest I will provide the URL of the old website that we are re-designing to work on.

Target Market(s)

People buying Jewellery

Number of Pages Required

1 page

Font styles to use
Sans Serif

Requirements
Must have
• Must be professional, and a fresher image then what we currently have.

```html
<!DOCTYPE html>
<html lang="en">
<head>
<meta charset="utf-8">
<title>Corvell Jewellers</title>
<link href="https://fonts.googleapis.com/css2?family=Tinos:wght@400;700&family=Arimo:wght@400&display=swap" rel="stylesheet">
<style>
:root{
  --ink:#111;
  --text:#333;
  --muted:#555;
  --rule:#999;
  --grey:#f1f1f1;
  --card:#fff;
  --line:#d8d8d8;
  --dark:#0d0d0d;
}
*{box-sizing:border-box;margin:0;padding:0}
html,body{width:1200px;height:4866px;overflow:hidden;background:#fff}
body{font-family:"Tinos","Times New Roman",serif;color:var(--text);position:relative}
.abs{position:absolute}
.heading{position:absolute;left:0;width:1200px;text-align:center;font-size:39px;font-weight:400;color:var(--ink);letter-spacing:.5px}
.heading::after{content:"";display:block;width:140px;height:2px;background:var(--rule);margin:18px auto 0}

/* nav */
.site-nav{position:absolute;top:0;left:0;width:1200px;height:96px;background:#fff;border-bottom:1px solid #eee}
.brand{position:absolute;left:75px;top:36px;font-size:21px;color:#444;letter-spacing:.3px}
.menu{position:absolute;top:42px;display:flex;gap:0;font-size:14px;color:#222;letter-spacing:.5px}
.menu a{position:absolute;white-space:nowrap;color:inherit;text-decoration:none}
.cart{position:absolute;left:1076px;top:36px}

/* hero */
.hero{position:absolute;top:96px;left:0;width:1200px;height:641px;background:linear-gradient(100deg,#6f6e6c 0%,#4a4946 35%,#3a3936 60%,#1c1c1b 100%)}
.hero-kicker{position:absolute;left:75px;top:300px;font-size:17px;color:#fff;font-weight:700;letter-spacing:1px}
.hero-title{position:absolute;left:73px;top:322px;font-size:66px;color:#fff;font-weight:700;letter-spacing:1px;line-height:1}
.hero-sub{position:absolute;left:75px;top:392px;width:640px;font-size:22px;color:#fff;font-weight:700;line-height:35px;letter-spacing:.5px}
.btn-outline-light{position:absolute;left:75px;top:484px;width:180px;height:46px;border:2px solid #fff;color:#fff;font-size:16px;line-height:42px;text-align:center;letter-spacing:.5px}

/* intro */
.intro-lead{position:absolute;top:898px;left:0;width:1200px;text-align:center;font-size:23px;color:#111}
.intro-body{position:absolute;top:952px;left:160px;width:880px;text-align:center;font-size:17px;line-height:33px;color:#444}

/* services */
.services{position:absolute;top:1115px;left:0;width:1200px;height:501px;background:var(--grey)}
.service{position:absolute;top:189px;width:243px;height:227px;background:var(--card);text-align:center}
.service svg{margin-top:30px}
.service h3{font-size:16px;font-weight:700;color:#111;letter-spacing:.6px;margin-top:22px}
.service a{display:inline-block;margin-top:17px;font-size:14px;color:#222;text-decoration:underline;letter-spacing:.5px}

/* collections */
.collection{position:absolute;top:1792px;width:252px;height:317px}
.collection span{position:absolute;left:18px;right:18px;bottom:30px;height:42px;background:rgba(240,240,240,.93);font-size:16px;font-weight:700;color:#111;text-align:center;line-height:42px;letter-spacing:.8px}

/* products */
.arrow{position:absolute;top:2448px}
.product{position:absolute;top:2291px;width:243px;text-align:center}
.product .shot{height:219px;border:1px solid var(--line)}
.product h4{font-size:15px;font-weight:400;color:#222;margin-top:21px;letter-spacing:.4px}
.product p{font-size:14px;color:#444;margin-top:7px}
.product .price{font-size:16px;font-weight:700;color:#111;margin-top:17px}
.product .add{width:34px;height:34px;border-radius:50%;background:var(--dark);margin:13px auto 0;display:flex;align-items:center;justify-content:center}

/* feature blocks */
.feature-panel{position:absolute;background:var(--grey)}
.feature-panel h2{font-size:40px;font-weight:400;color:#222;letter-spacing:.5px}
.feature-panel p{font-size:14.5px;line-height:29px;color:#222;margin-top:28px}
.btn-outline{display:block;width:182px;height:46px;border:1.5px solid #555;font-size:18px;line-height:43px;text-align:center;color:#222;margin-top:28px;letter-spacing:.5px}

/* reviews */
.reviews{position:absolute;top:3791px;left:0;width:1200px;height:471px;background:var(--grey)}
.review{position:absolute;top:156px;width:340px;text-align:center}
.stars{font-size:17px;letter-spacing:3px;color:#111}
.review p{font-size:14.5px;line-height:27px;color:#333;margin-top:12px}
.review h5{font-size:13.5px;font-weight:700;color:#111;margin-top:22px;letter-spacing:.6px}
.dots{position:absolute;top:398px;left:570px;display:flex;gap:8px}
.dots i{width:12px;height:12px;border-radius:50%;background:#bbb;display:block}
.dots i:first-child{background:#111}

/* mailing */
.mail-note{position:absolute;top:4414px;left:0;width:1200px;text-align:center;font-size:15px;color:#222}
.mail-input{position:absolute;top:4454px;left:308px;width:450px;height:44px;border:1px solid #ccc;font-family:"Arimo",Arial,sans-serif;font-size:13px;color:#333;line-height:42px;padding-left:16px}
.mail-btn{position:absolute;top:4454px;left:770px;width:105px;height:44px;background:var(--dark);color:#fff;font-family:"Arimo",Arial,sans-serif;font-size:13px;line-height:44px;text-align:center}

/* footer */
.site-footer{position:absolute;top:4570px;left:0;width:1200px;height:296px;background:var(--grey);font-size:12.5px;color:#444}
.site-footer h6{position:absolute;font-size:14px;font-weight:400;color:#333;letter-spacing:.6px}
.site-footer ul{position:absolute;list-style:none;line-height:28.5px}
.contact-line{position:absolute;display:flex;align-items:center;gap:14px}
.social{position:absolute;top:95px;left:919px;display:flex;gap:10px}
.social i{width:33px;height:33px;border:1.5px solid #444;border-radius:50%;display:block}
</style>
</head>
<body>

<header class="site-nav">
  <div class="brand">CORVELL JEWELLERS</div>
  <nav class="menu">
    <a style="left:353px">ENGAGEMENT</a>
    <a style="left:512px">FINE JEWELLERY</a>
    <a style="left:690px">DESIGNERS</a>
    <a style="left:827px">WATCHES</a>
    <a style="left:950px">ABOUT US</a>
  </nav>
  <svg class="cart" width="44" height="30" viewBox="0 0 44 30" aria-label="Basket">
    <path d="M2 10h24l-3 12H5z" fill="#111"/>
    <path d="M8 10l5-7M20 10l-5-7" stroke="#111" stroke-width="2" fill="none"/>
    <circle cx="36" cy="6" r="6" fill="#ddd"/>
    <text x="36" y="10" font-size="10" text-anchor="middle" fill="#111" font-family="Arimo,sans-serif">0</text>
  </svg>
</header>

<section class="hero" role="img" aria-label="Close-up of fingers holding a diamond ring while tweezers set a stone">
  <div class="hero-kicker">LET US BRING YOUR IDEAS TO LIFE WITH</div>
  <div class="hero-title">CUSTOM DESIGNS</div>
  <div class="hero-sub">Create a bespoke heirloom to be passed on through the generations.</div>
  <div class="btn-outline-light">READ MORE</div>
</section>

<h2 class="heading" style="top:812px">WHAT WE DO</h2>
<p class="intro-lead">Let us be your one stop shop for all your jewellery, watches, repairs and design needs.</p>
<p class="intro-body">Here at Corvell we like to think of ourselves as all rounders being able to help our customers with all Jewellery design and remake needs, jewellery repairs, and watch repairs. Aswell as selling some of New Zealand's and the worlds top jewellery and watch brands.</p>

<section class="services">
  <h2 class="heading" style="top:73px">WHAT WE DO</h2>
  <div class="service" style="left:75px">
    <svg width="90" height="80" viewBox="0 0 90 80" fill="none" stroke="#111" stroke-width="3"><path d="M25 10h40l12 14-32 30-32-30z"/><path d="M13 24h64M35 10l-5 14 15 30 15-30-5-14"/><path d="M8 40c2 14 14 24 28 32M82 40c-2 14-14 24-28 32"/></svg>
    <h3>DIAMOND BROKERS</h3><a>READ MORE</a>
  </div>
  <div class="service" style="left:345px">
    <svg width="90" height="80" viewBox="0 0 90 80" fill="none" stroke="#111" stroke-width="3"><circle cx="40" cy="50" r="24"/><circle cx="40" cy="50" r="17"/><path d="M32 20l8-10 8 10-8 6z"/><path d="M66 36c8 4 10 20 2 30"/></svg>
    <h3>DESIGN &amp; REMAKES</h3><a>READ MORE</a>
  </div>
  <div class="service" style="left:615px">
    <svg width="90" height="80" viewBox="0 0 90 80" fill="none" stroke="#111" stroke-width="3"><circle cx="38" cy="50" r="24"/><circle cx="38" cy="50" r="17"/><path d="M54 28l12-12 8 8-12 12z"/><path d="M66 8l3 4M76 12l-4 3"/></svg>
    <h3>JEWELLERY REPAIRS</h3><a>READ MORE</a>
  </div>
  <div class="service" style="left:885px">
    <svg width="90" height="80" viewBox="0 0 90 80" fill="none" stroke="#111" stroke-width="3"><rect x="32" y="4" width="26" height="12"/><rect x="32" y="64" width="26" height="12"/><circle cx="45" cy="40" r="24"/><path d="M45 26v14l-8 6M21 40h6"/><path d="M60 22l8-8"/></svg>
    <h3>WATCH REPAIRS</h3><a>READ MORE</a>
  </div>
</section>

<h2 class="heading" style="top:1669px">OUR COLLECTIONS</h2>
<div class="collection" style="left:75px;background:linear-gradient(135deg,#555 0%,#2a2a2a 55%,#0e0e0e 100%)" role="img" aria-label="Diamond solitaire engagement ring"><span>ENGAGEMENT</span></div>
<div class="collection" style="left:341px;background:linear-gradient(135deg,#d8d8d6 0%,#a9a6a2 45%,#6b5a50 100%)" role="img" aria-label="Cufflink on a white shirt cuff"><span>FINE JEWELLERY</span></div>
<div class="collection" style="left:608px;background:linear-gradient(135deg,#f2f2f0 0%,#dcdcda 50%,#b9b9b7 100%)" role="img" aria-label="Designer at a desk working on jewellery"><span>DESIGNERS</span></div>
<div class="collection" style="left:874px;background:linear-gradient(135deg,#1a1a1a 0%,#2c2624 50%,#050505 100%)" role="img" aria-label="Chronograph wrist watch on black"><span>WATCHES</span></div>

<h2 class="heading" style="top:2170px">FEATURED PRODUCTS</h2>
<svg class="arrow" style="left:44px" width="16" height="28" viewBox="0 0 16 28"><path d="M14 2L3 14l11 12" fill="none" stroke="#333" stroke-width="2"/></svg>
<svg class="arrow" style="left:1140px" width="16" height="28" viewBox="0 0 16 28"><path d="M2 2l11 12L2 26" fill="none" stroke="#333" stroke-width="2"/></svg>

<div class="product" style="left:75px">
  <div class="shot" role="img" aria-label="Pair of black and rose gold cufflinks" style="background:radial-gradient(circle at 50% 50%,#9a8f8a 0%,#fff 60%)"></div>
  <h4>PRODUCT NAME</h4><p>Duis aliquam nibh a dui</p><div class="price">$25.00</div>
  <div class="add"><svg width="16" height="14" viewBox="0 0 16 14"><path d="M0 1h3l2 8h8l2-6H4" fill="none" stroke="#fff" stroke-width="1.6"/><circle cx="6" cy="12" r="1.3" fill="#fff"/><circle cx="12" cy="12" r="1.3" fill="#fff"/></svg></div>
</div>
<div class="product" style="left:345px">
  <div class="shot" role="img" aria-label="Silver ring with a square cut stone" style="background:radial-gradient(circle at 50% 50%,#c9c2bd 0%,#fff 60%)"></div>
  <h4>PRODUCT NAME</h4><p>Duis aliquam nibh a dui</p><div class="price">$25.00</div>
  <div class="add"><svg width="16" height="14" viewBox="0 0 16 14"><path d="M0 1h3l2 8h8l2-6H4" fill="none" stroke="#fff" stroke-width="1.6"/><circle cx="6" cy="12" r="1.3" fill="#fff"/><circle cx="12" cy="12" r="1.3" fill="#fff"/></svg></div>
</div>
<div class="product" style="left:615px">
  <div class="shot" role="img" aria-label="Steel bracelet watch with white dial" style="background:radial-gradient(circle at 50% 50%,#b8b8b8 0%,#fff 60%)"></div>
  <h4>PRODUCT NAME</h4><p>Duis aliquam nibh a dui</p><div class="price">$25.00</div>
  <div class="add"><svg width="16" height="14" viewBox="0 0 16 14"><path d="M0 1h3l2 8h8l2-6H4" fill="none" stroke="#fff" stroke-width="1.6"/><circle cx="6" cy="12" r="1.3" fill="#fff"/><circle cx="12" cy="12" r="1.3" fill="#fff"/></svg></div>
</div>
<div class="product" style="left:885px">
  <div class="shot" role="img" aria-label="Silver chain charm bracelet" style="background:radial-gradient(circle at 50% 50%,#a8a8a8 0%,#ddd 70%)"></div>
  <h4>PRODUCT NAME</h4><p>Duis aliquam nibh a dui</p><div class="price">$25.00</div>
  <div class="add"><svg width="16" height="14" viewBox="0 0 16 14"><path d="M0 1h3l2 8h8l2-6H4" fill="none" stroke="#fff" stroke-width="1.6"/><circle cx="6" cy="12" r="1.3" fill="#fff"/><circle cx="12" cy="12" r="1.3" fill="#fff"/></svg></div>
</div>

<div class="abs" style="left:75px;top:2725px;width:600px;height:463px;background:linear-gradient(135deg,#9eaab0 0%,#d9dde2 45%,#e9e6ec 100%)" role="img" aria-label="Pencil sketches of necklace designs on paper"></div>
<div class="feature-panel" style="left:525px;top:2776px;width:675px;height:361px;padding:38px 0 0 33px">
  <h2>BESPOKE</h2>
  <p style="width:570px">Let us help you create a one of a kind, unique, bespoke piece to pass on through the generations as your family heirloom. Here at corvell we will work hard to bring your vision &amp; design to life. Our process is using our state of the art design system to design &amp; then handmake your piece right here in auckland, new zealand.</p>
  <div class="btn-outline">READ MORE</div>
</div>

<div class="abs" style="left:525px;top:3251px;width:601px;height:461px;background:radial-gradient(circle at 55% 70%,#9a9a9a 0%,#3a3a3a 35%,#141414 75%)" role="img" aria-label="Loose round brilliant diamond on dark surface"></div>
<div class="feature-panel" style="left:0;top:3302px;width:677px;height:359px;padding:36px 0 0 73px">
  <h2>BROKER</h2>
  <p style="width:575px">With any bespoke design it all starts with the stone. Whether this be diamonds or coloured stone we will be able to source the best options for you to choose from at wholesale pricing. We travel, handpicking stones from the worlds leading agencies in belgium, america, hong kong &amp; australia.</p>
  <div class="btn-outline">READ MORE</div>
</div>

<section class="reviews">
  <h2 class="heading" style="top:70px">CUSTOMER REVIEWS</h2>
  <div class="review" style="left:70px"><div class="stars">★★★★★</div><p>“ Aliquam molestie, mi et imperdiet euismod, dui purus auctor tellus, et interdum lacus lectus et ante. Sed accumsan sollicitudin sapien, sit amet adipiscing turpis gravida ac...”</p><h5>-NAME HEADING</h5></div>
  <div class="review" style="left:430px"><div class="stars">★★★★★</div><p>“ Aliquam molestie, mi et imperdiet euismod, dui purus auctor tellus, et interdum lacus lectus et ante. Sed accumsan sollicitudin sapien, sit amet adipiscing turpis gravida ac...”</p><h5>-NAME HEADING</h5></div>
  <div class="review" style="left:790px"><div class="stars">★★★★★</div><p>“ Aliquam molestie, mi et imperdiet euismod, dui purus auctor tellus, et interdum lacus lectus et ante. Sed accumsan sollicitudin sapien, sit amet adipiscing turpis gravida ac...”</p><h5>-NAME HEADING</h5></div>
  <div class="dots"><i></i><i></i><i></i></div>
</section>

<h2 class="heading" style="top:4315px">JOIN OUR MAILING LIST</h2>
<p class="mail-note">Keep up to date with our latest arrivals and Promotions.</p>
<div class="mail-input">Email Address</div>
<div class="mail-btn">JOIN NOW</div>

<footer class="site-footer">
  <h6 style="left:75px;top:52px">SITE MAP</h6>
  <ul style="left:75px;top:76px"><li>Engagement</li><li>Fine Jewellery</li><li>Designers</li><li>Watches</li><li>About Us</li></ul>
  <h6 style="left:256px;top:52px">FINANCE</h6>
  <ul style="left:256px;top:76px"><li>Bramley Finance</li><li>Splitway</li></ul>
  <h6 style="left:425px;top:52px">TERMS &amp; CONDITIONS</h6>
  <ul style="left:425px;top:76px"><li>Terms &amp; Conditions</li><li>Jewellery Care</li></ul>
  <h6 style="left:425px;top:160px">CONTACT US</h6>
  <ul style="left:425px;top:184px"><li>Store Locator</li></ul>
  <h6 style="left:666px;top:52px">CONTACT INFO</h6>
  <div class="abs" style="left:666px;top:80px">18 Marlow Street, Ashgrove</div>
  <div class="contact-line" style="left:666px;top:106px"><svg width="14" height="14" viewBox="0 0 14 14"><path d="M3 1l3 3-2 2c1 2 2 3 4 4l2-2 3 3-2 2C6 13 1 8 1 3z" fill="#111"/></svg><span style="margin-left:8px">09 412 6630</span></div>
  <div class="abs" style="left:666px;top:142px;line-height:22px">Unit 4b, 12 Harlan Road,<br>Westbrook Village</div>
  <div class="contact-line" style="left:666px;top:198px"><svg width="14" height="14" viewBox="0 0 14 14"><path d="M3 1l3 3-2 2c1 2 2 3 4 4l2-2 3 3-2 2C6 13 1 8 1 3z" fill="#111"/></svg><span style="margin-left:8px">09 455 7128</span></div>
  <div class="contact-line" style="left:666px;top:226px"><svg width="14" height="12" viewBox="0 0 14 12"><rect width="14" height="12" fill="#111"/><path d="M0 1l7 5 7-5" stroke="#fff" fill="none"/></svg><span style="margin-left:8px">info@corvelljewellers.example.nz</span></div>
  <h6 style="left:919px;top:52px">FOLLOW US</h6>
  <div class="social"><i></i><i></i><i></i><i></i></div>
  <div class="abs" style="left:919px;top:170px;line-height:22px">Copyright © 2021. Company Name<br>All Right Reserved</div>
</footer>

</body>
</html>
```